New Peanut Butter Brand Needs Product Label

We need a packaging label for a new to market peanut butter product based in the UK. The range of peanut butters will include a range of great flavours. We have been looking at labels to give inspiration and we are liking the less complicated designs that are on a white background (Sample designs are attached).

The company is called 'Breezy Acorn Company' The name could be used in full or shortened to 'Breezy Acorn Co'

The design should be a little fun and cool (not in a childish way), using bright colours and a mixture of fonts would be fine (as long as the text is easy to read)

For the purposes of this design brief text that should be added to the front of the design is

Brand name (As above)
Sea Salt (The flavour of this product)
Chunky (Peanut butter is chunky or smooth right !!)

Allowance should be given for the ingredients panel and standard information used on a food product.

Key phrases that could be used in the design are below

Great source of protein
Heart Healthy
Packed with nutrients

The food container will be a plastic pot and so the labels are slightly curved. I have attached a picture of a similar pot and a label outline an sizing which should be of help.

```html
<!DOCTYPE html>
<html lang="en">
<head>
<meta charset="utf-8">
<title>Breezy Acorn Co – Chunky Peanut Butter Label</title>
<link rel="stylesheet" href="https://fonts.googleapis.com/css2?family=Fredoka:wght@600&family=Open+Sans:wght@600;700&display=swap">
<style>
  :root {
    --backdrop-top: #3b6699;
    --backdrop-bottom: #c9d6e4;
    --navy: #173f7e;
    --navy-light: #2a5ea8;
    --sky: #1a7fd0;
    --sky-light: #19b8e6;
    --label-white: #ffffff;
    --label-grey: #e3e6ea;
    --flavour-purple: #7b5a9e;
    --wave-red: #d1262f;
    --wave-green: #2f8a2f;
  }
  * { margin: 0; padding: 0; box-sizing: border-box; }
  html, body { width: 1200px; height: 600px; overflow: hidden; }
  body {
    background: linear-gradient(180deg, var(--backdrop-top) 0%, var(--backdrop-bottom) 100%);
    position: relative;
  }
  .label {
    position: absolute;
    top: 120px;
    width: 500px;
    height: 360px;
    filter: drop-shadow(0 6px 12px rgba(0, 0, 0, 0.25));
  }
  .label--classic { left: 70px; }
  .label--green-trim { left: 630px; }
  .band-text {
    font-family: "Open Sans", sans-serif;
    font-weight: 700;
    fill: var(--label-white);
  }
  .tagline { font-size: 15px; letter-spacing: 2px; }
  .flavour { font-size: 24px; font-weight: 600; letter-spacing: 1.5px; }
  .brand-name {
    font-family: "Open Sans", sans-serif;
    font-weight: 700;
    font-size: 40px;
    fill: var(--navy);
  }
  .product-name {
    font-family: "Fredoka", sans-serif;
    font-weight: 600;
    font-size: 27px;
    fill: var(--flavour-purple);
  }
  .wave-red { fill: none; stroke: var(--wave-red); stroke-width: 3; }
  .wave-green { fill: none; stroke: var(--wave-green); stroke-width: 3.5; }
</style>
</head>
<body>

<svg class="label label--classic" viewBox="0 0 500 360" aria-label="Sea Salt chunky peanut butter label, classic trim">
  <defs>
    <linearGradient id="navyBand" x1="0" x2="1">
      <stop offset="0" stop-color="var(--navy)"/>
      <stop offset="0.5" stop-color="var(--navy-light)"/>
      <stop offset="1" stop-color="var(--navy)"/>
    </linearGradient>
    <linearGradient id="skyBand" x1="0" x2="1">
      <stop offset="0" stop-color="var(--sky)"/>
      <stop offset="0.5" stop-color="var(--sky-light)"/>
      <stop offset="1" stop-color="var(--sky)"/>
    </linearGradient>
  </defs>
  <rect class="label-body" width="500" height="360" fill="var(--label-white)"/>
  <path class="top-band" d="M0 0 H500 V40 Q437 56 375 42 T250 42 T125 42 T0 42 Z" fill="url(#navyBand)"/>
  <text class="band-text tagline" x="250" y="28" text-anchor="middle">PACKED WITH NUTRIENTS</text>
  <text class="brand-name" x="250" y="148" text-anchor="middle">Breezy Acorn Co</text>
  <path class="wave-red" d="M80 212 Q100 204 120 212 T160 212 T200 212 T240 212 T280 212 T320 212 T360 212 T400 212 T420 210"/>
  <text class="product-name" x="250" y="246" text-anchor="middle">Chunky Peanut Butter</text>
  <path class="bottom-band" d="M0 272 Q62 258 125 270 T250 270 T375 270 T500 270 V330 H0 Z" fill="url(#skyBand)"/>
  <text class="band-text flavour" x="250" y="312" text-anchor="middle">Sea Salt Flavour</text>
  <rect class="base-strip" y="330" width="500" height="30" fill="var(--label-grey)"/>
</svg>

<svg class="label label--green-trim" viewBox="0 0 500 360" aria-label="Sea Salt chunky peanut butter label, green trim">
  <defs>
    <linearGradient id="navyBandB" x1="0" x2="1">
      <stop offset="0" stop-color="var(--navy)"/>
      <stop offset="0.5" stop-color="var(--navy-light)"/>
      <stop offset="1" stop-color="var(--navy)"/>
    </linearGradient>
    <linearGradient id="skyBandB" x1="0" x2="1">
      <stop offset="0" stop-color="var(--sky)"/>
      <stop offset="0.5" stop-color="var(--sky-light)"/>
      <stop offset="1" stop-color="var(--sky)"/>
    </linearGradient>
  </defs>
  <rect class="label-body" width="500" height="360" fill="var(--label-white)"/>
  <path class="top-band" d="M0 0 H500 V40 Q437 56 375 42 T250 42 T125 42 T0 42 Z" fill="url(#navyBandB)"/>
  <path class="wave-green" d="M0 51 Q62 65 125 51 T250 51 T375 51 T500 49"/>
  <text class="band-text tagline" x="250" y="28" text-anchor="middle">PACKED WITH NUTRIENTS</text>
  <text class="brand-name" x="250" y="148" text-anchor="middle">Breezy Acorn Co</text>
  <path class="wave-red" d="M80 212 Q100 204 120 212 T160 212 T200 212 T240 212 T280 212 T320 212 T360 212 T400 212 T420 210"/>
  <text class="product-name" x="250" y="246" text-anchor="middle">Chunky Peanut Butter</text>
  <path class="wave-green" d="M0 262 Q62 250 125 260 T250 260 T375 260 T500 258"/>
  <path class="bottom-band" d="M0 272 Q62 258 125 270 T250 270 T375 270 T500 270 V330 H0 Z" fill="url(#skyBandB)"/>
  <text class="band-text flavour" x="250" y="312" text-anchor="middle">Sea Salt Flavour</text>
  <rect class="base-strip" y="330" width="500" height="30" fill="var(--label-grey)"/>
</svg>

</body>
</html>
```